Bodywork Quietude Business Card Design

I want to create a very elegant and sophisticated two sided business card for my massage practice (www.bodyworkquietude.net). I have attached the logo and a PDF with some ideas down for the back of the card but I am open to suggestions. I will want to tie in a post card and flyer to the card later.
Similar colors to website would be great.
Target Market(s)
High end clientele, people looking for a sophisticated spa experience.
Industry/Entity Type
Massage
Contact Information for Business Card
Bodywork Quietude
7318 Larkspur Ave S, Suite 305
Seattle, WA 98103
(206) 555-0147
www.bodyworkquietude.net
Look and feel

```html
<!DOCTYPE html>
<html lang="en">
<head>
<meta charset="utf-8">
<title>Bodywork Quietude – Business Card</title>
<link rel="stylesheet" href="https://fonts.googleapis.com/css2?family=Cormorant+Garamond:wght@500&family=Raleway:wght@400&display=swap">
<style>
  :root {
    --backdrop: #e9eaeb;
    --card-light: #ffffff;
    --navy: #1a2f3f;
    --cream: #eee6da;
    --ink-light: #e6e9ec;
  }
  * { margin: 0; padding: 0; box-sizing: border-box; }
  html, body { width: 1200px; height: 1000px; overflow: hidden; }
  body { background: var(--backdrop); position: relative; }

  .card {
    position: absolute;
    left: 240px;
    width: 696px;
    height: 395px;
    border-radius: 14px;
    overflow: hidden;
    box-shadow: 0 2px 8px rgba(0,0,0,0.12);
  }
  .card--front { top: 83px; background: var(--card-light); }
  .card--back { top: 521px; background: var(--navy); }

  .brand {
    position: absolute;
    left: 0; right: 0;
    display: flex;
    flex-direction: column;
    align-items: center;
    font-family: "Cormorant Garamond", "Times New Roman", serif;
    font-weight: 500;
    text-transform: uppercase;
    letter-spacing: 0.01em;
    line-height: 1;
  }
  .brand__mark {
    border-radius: 50%;
    border: 2px solid currentColor;
  }
  .card--front .brand { top: 72px; color: var(--navy); font-size: 30px; gap: 26px; }
  .card--front .brand__mark { width: 54px; height: 54px; }
  .card--back .brand { top: 104px; color: var(--cream); font-size: 40px; gap: 34px; }
  .card--back .brand__mark { width: 72px; height: 72px; }

  .contact-band {
    position: absolute;
    left: 0; right: 0; bottom: 0;
    height: 78px;
    background: var(--navy);
    color: var(--ink-light);
    font-family: "Raleway", "Helvetica Neue", Arial, sans-serif;
    font-size: 15px;
    letter-spacing: 0.02em;
    text-align: center;
    display: flex;
    flex-direction: column;
    justify-content: center;
    gap: 6px;
  }
</style>
</head>
<body>
  <section class="card card--front">
    <div class="brand">
      <span class="brand__mark"></span>
      <span class="brand__name">Bodywork Quietude</span>
    </div>
    <footer class="contact-band">
      <p class="contact-band__line">(206) 555-0147 | www.bodyworkquietude.net</p>
      <p class="contact-band__line">7318 Larkspur Ave S, Suite 305 Seattle, WA 98103</p>
    </footer>
  </section>

  <section class="card card--back">
    <div class="brand">
      <span class="brand__mark"></span>
      <span class="brand__name">Bodywork Quietude</span>
    </div>
  </section>
</body>
</html>
```